Mental Health Clinic Website

website for a mental health clinic. two files describing the website are attached, in case of conflicting info the word document is priority.

Target Market(s)

Ohio / Pennsylvania residents

Industry/Entity Type

Health Care

Coding

Coded - Design and coding required

Number of Pages Required

5+ page

Requirements
Must have
• see attached

```html
<!DOCTYPE html>
<html lang="en">
<head>
<meta charset="utf-8">
<title>Dr Ellery Harmony Center</title>
<link href="https://fonts.googleapis.com/css2?family=Nunito:wght@400;600;700;800&family=Open+Sans:wght@400;600;700&display=swap" rel="stylesheet">
<style>
:root{
  --yellow:#f5c400;
  --red:#d8262b;
  --green:#5d9e32;
  --lime:#8bc53f;
  --navy:#1a3a8f;
  --ink:#333;
  --grey-card:#e9e9e9;
  --bar:#3d3f42;
  --foot:#1c2431;
  --orange:#f07d1a;
  --link-blue:#2d5ea8;
  --svc-blue:#8fb4ff;
}
*{box-sizing:border-box;margin:0;padding:0}
html,body{width:1200px;height:3854px;overflow:hidden}
body{font-family:"Open Sans",sans-serif;color:var(--ink);background:#fff;position:relative}
h1,h2,h3,h4{font-family:"Nunito",sans-serif}
section,header,footer{position:absolute;left:0;width:1200px}

/* hero */
.hero{top:0;height:615px;overflow:hidden;
  background:
    radial-gradient(ellipse 260px 330px at 640px 330px,rgba(214,190,160,.55),rgba(214,190,160,0) 70%),
    radial-gradient(ellipse 500px 200px at 700px 120px,rgba(235,230,170,.55),rgba(235,230,170,0) 70%),
    linear-gradient(180deg,#55612c 0%,#7c8740 28%,#4f6a26 55%,#35521b 78%,#2a4315 100%)}
.hero-photo{position:absolute;inset:0}
.logo-disc{position:absolute;left:64px;top:-78px;width:282px;height:282px;border-radius:50%;background:#fff;display:flex;align-items:flex-end;justify-content:center;padding-bottom:58px}
.logo-disc span{font-family:"Nunito",sans-serif;font-weight:600;font-size:11px;color:#2b2b2b}
.nav{position:absolute;right:145px;top:10px;display:flex;gap:30px}
.nav a{color:#fff;text-decoration:none;font-size:14px}
.nav a.active{color:var(--yellow)}
.hero-title{position:absolute;left:145px;top:283px;color:var(--yellow)}
.hero-title .line1{font-family:"Nunito",sans-serif;font-size:30px;font-weight:400;line-height:1.2}
.hero-title .line2{font-family:"Nunito",sans-serif;font-size:31px;font-weight:800;letter-spacing:.5px;line-height:1.25}
.arrow{position:absolute;top:290px;width:34px;height:34px;border-radius:50%;background:var(--orange)}
.arrow svg{display:block}

/* welcome */
.welcome{top:615px;height:490px}
.welcome h2{position:absolute;left:145px;top:68px;font-size:42px;font-weight:400;color:var(--red)}
.welcome .copy{position:absolute;left:145px;top:130px;width:560px;font-size:12px;line-height:1.6;color:#444}
.welcome .copy p{margin-bottom:18px}
.welcome .portrait{position:absolute;left:727px;top:80px;width:330px;height:330px;border-radius:50%;
  background:
    radial-gradient(ellipse 90px 120px at 50% 62%,rgba(200,110,70,.75),rgba(200,110,70,0) 75%),
    radial-gradient(ellipse 80px 90px at 50% 85%,rgba(90,130,190,.8),rgba(90,130,190,0) 80%),
    radial-gradient(circle at 50% 35%,#efd9b8,#e6c9a6 45%,#c9d0d8 100%)}

/* about */
.about{top:1105px;height:805px;background:linear-gradient(180deg,#23262b,#1b1e22 60%,#2a2c2f);color:#ddd;text-align:center}
.about-glow{position:absolute;left:440px;top:180px;width:320px;height:360px;border-radius:50%;background:radial-gradient(ellipse,rgba(170,125,90,.45),rgba(0,0,0,0) 70%)}
.about h2{position:absolute;top:20px;width:100%;font-size:40px;font-weight:400;color:var(--yellow)}
.about .intro{position:absolute;left:145px;top:75px;width:910px;font-size:12px;line-height:1.6}
.about .ages{position:absolute;top:115px;width:100%;color:var(--lime);font-weight:700;font-size:14px}
.about .lang-note{position:absolute;top:157px;width:100%;font-size:11.5px}
.langs{position:absolute;top:178px;width:100%;display:flex;justify-content:center;gap:28px;font-weight:600;font-size:15px;color:#fff}
.langs span{display:flex;align-items:center;gap:6px}
.langs svg{display:block}
.about h3{position:absolute;top:365px;width:100%;font-size:38px;font-weight:400;color:var(--yellow)}
.team{position:absolute;left:145px;top:430px;display:flex;gap:17px}
.member{width:170px;height:350px;background:#fff;position:relative;text-align:center}
.member .photo{height:180px;background:radial-gradient(ellipse 60px 70px at 50% 45%,#c99672,#a9795a 50%,rgba(90,90,90,0) 100%),radial-gradient(ellipse 80px 50px at 50% 100%,#e9e9e9,rgba(200,200,200,0) 100%),linear-gradient(180deg,#6d6d6d,#3f3f3f)}
.member .photo.warm{background:radial-gradient(ellipse 60px 75px at 50% 45%,#e2b48e,#b57c56 55%,rgba(90,90,90,0) 100%),radial-gradient(ellipse 80px 50px at 50% 100%,#2d2d2d,rgba(40,40,40,0) 100%),linear-gradient(180deg,#7a7a7a,#4a4a4a)}
.member h4{font-size:15px;font-weight:400;color:var(--link-blue);margin-top:18px}
.member .role{font-size:10.5px;color:#444;margin-top:2px}
.member .bio{font-size:9px;color:#888;line-height:1.45;padding:10px 14px 0}
.member .book{position:absolute;bottom:0;left:0;right:0;height:28px;background:var(--green);color:#fff;font-size:10px;font-weight:600;line-height:28px}

/* services */
.services{top:1910px;height:385px;background:var(--navy)}
.services h2{position:absolute;left:145px;top:30px;font-size:38px;font-weight:400;color:var(--yellow)}
.svc-list{position:absolute;left:145px;top:95px;list-style:none;width:450px}
.svc-list li{display:flex;align-items:center;height:56px;font-size:14px;color:var(--svc-blue)}
.svc-list li.current{color:#fff}
.svc-list li svg{margin-right:16px;flex:none}
.svc-list li.current::after{content:"";flex:1;height:1px;background:rgba(255,255,255,.5);margin-left:20px}
.svc-photo{position:absolute;left:600px;top:0;width:600px;height:385px;
  background:
    radial-gradient(ellipse 120px 90px at 420px 200px,rgba(235,240,250,.9),rgba(235,240,250,0) 80%),
    radial-gradient(ellipse 160px 160px at 120px 100px,#f5f6f8,rgba(240,240,240,0) 80%),
    linear-gradient(100deg,#e9ecf0 0%,#d9dee5 45%,#7fa4c9 80%,#3c6aa0 100%)}
.svc-caption{position:absolute;left:600px;top:250px;width:600px;height:135px;background:rgba(20,20,25,.85);color:#fff;padding:18px 22px}
.svc-caption h3{font-size:23px;font-weight:700;letter-spacing:.5px}
.svc-caption p{font-size:10.5px;line-height:1.5;margin-top:8px;color:#ddd;width:440px}

/* reads */
.reads{top:2295px;height:615px}
.reads h2{position:absolute;top:65px;width:100%;text-align:center;font-size:38px;font-weight:400;color:var(--red)}
.post{position:absolute;left:145px;width:910px;height:192px;background:var(--grey-card);display:flex}
.post .thumb{width:320px;height:192px;flex:none}
.thumb.book{background:repeating-linear-gradient(170deg,#f7f7f7 0 6px,#cfcfcf 6px 7px),linear-gradient(180deg,#fff,#999)}
.thumb.mags{background:repeating-linear-gradient(100deg,#f4f1ea 0 5px,#d7b76a 5px 7px,#8fb3d8 7px 9px,#f0f0f0 9px 14px)}
.post .body{padding:28px 28px 0}
.post h3{font-size:17px;font-weight:600;color:#222}
.post .author{font-size:10.5px;color:#444;margin-top:6px}
.post p{font-size:10.5px;line-height:1.6;color:#555;margin-top:12px}
.post .more{font-size:10px;font-weight:700;text-decoration:underline;color:#222}

/* appointment */
.appointment{top:2910px;height:455px;background:var(--navy)}
.appointment h2{position:absolute;top:65px;width:100%;text-align:center;font-size:38px;font-weight:400;color:var(--yellow)}
.field{position:absolute;background:#fff;font-size:10.5px;color:#888;padding:9px 10px}
.submit{position:absolute;left:553px;top:330px;width:95px;height:36px;border-radius:18px;background:var(--yellow);color:#222;font-weight:600;font-size:14px;text-align:center;line-height:36px}

/* map */
.map{top:3365px;height:335px;background:linear-gradient(135deg,#eceeea,#e4e7e2 50%,#ececec)}
.map .pin{position:absolute;left:590px;top:170px}

/* contact bar + footer */
.contact-bar{position:absolute;left:0;top:3700px;width:1200px;height:58px;background:var(--bar);color:#fff;font-size:14px;display:flex;align-items:center;justify-content:center;gap:90px}
.contact-bar span{display:flex;align-items:center;gap:7px}
.site-footer{top:3758px;height:96px;background:var(--foot);color:#aab;font-size:10.5px}
.foot-mark{position:absolute;left:145px;top:24px;width:34px;height:34px;border-radius:50%;background:#3a4556}
.foot-links{position:absolute;left:215px;top:24px;display:flex;gap:10px;color:#ccd}
.foot-links i{font-style:normal;color:#667}
.copyright{position:absolute;left:215px;top:48px}
.social{position:absolute;right:145px;top:30px;display:flex;gap:8px}
.social span{width:22px;height:22px;border-radius:50%;background:#2d7fd0}
</style>
</head>
<body>

<header class="hero">
  <div class="hero-photo" role="img" aria-label="Man meditating cross-legged in a sunlit grassy field with trees behind"></div>
  <div class="logo-disc"><span>Dr Ellery Harmony Center</span></div>
  <nav class="nav">
    <a class="active" href="#">Home</a><a href="#">About Us</a><a href="#">Services</a><a href="#">Good Reads</a><a href="#">Contact</a>
  </nav>
  <div class="hero-title">
    <div class="line1">Dr Ellery</div>
    <div class="line2">HARMONY CENTER</div>
  </div>
  <div class="arrow" style="left:52px"><svg width="34" height="34"><path d="M19 10l-7 7 7 7" fill="none" stroke="#fff" stroke-width="3"/></svg></div>
  <div class="arrow" style="left:1112px"><svg width="34" height="34"><path d="M15 10l7 7-7 7" fill="none" stroke="#fff" stroke-width="3"/></svg></div>
</header>

<section class="welcome">
  <h2>Welcome</h2>
  <div class="copy">
    <p>Each individual is unique with unique personality and unique needs. Therefore we provide individual treatment customized for you or your child. Multiculturalism also informs our practice. We are a full service mental health practice with the capacity to serve adults, children, teens and their parents.</p>
    <p>We provide high quality evidence based treatment and care including medication management, pharmacogenomic testing, individual psychotherapy, group psychotherapy, art therapy, CBT, DBT and trauma therapy. Our providers are experts in treating variety of illnesses such as depression, anxiety, schizophrenia, ADHD, gender identity concerns and PTSD.</p>
    <p>We are experienced in a variety of methods that help people achieve their psychological goals, and we will discuss with you the best ways to attain the health and wellness that you deserve. We are committed to helping you achieve your optimal level of emotional functioning and fulfill a successful life.</p>
  </div>
  <div class="portrait" role="img" aria-label="Smiling red-haired woman with eyes closed framed by a soft colourful tree canopy"></div>
</section>

<section class="about">
  <div class="about-glow" role="img" aria-label="Softly lit woman in a calm dark interior"></div>
  <h2>About Us</h2>
  <p class="intro">You will find a number of highly specialized – experienced and caring therapists and psychiatrists in Harmony Center. We provide medication management and psychotherapy (counseling) across the lifespan.</p>
  <p class="ages">– CHILDREN, TEENS AND ADULTS.</p>
  <p class="lang-note">Other than English, we speak the following languages</p>
  <div class="langs">
    <span><svg width="18" height="12"><rect width="18" height="12" fill="#c60b1e"/><rect y="3" width="18" height="6" fill="#ffc400"/></svg>Spanish</span>
    <span><svg width="18" height="12"><rect width="18" height="4" fill="#000"/><rect y="4" width="18" height="4" fill="#dd0000"/><rect y="8" width="18" height="4" fill="#ffce00"/></svg>German</span>
    <span><svg width="18" height="12"><rect width="18" height="4" fill="#239f40"/><rect y="4" width="18" height="4" fill="#fff"/><rect y="8" width="18" height="4" fill="#da0000"/></svg>Farsi</span>
    <span><svg width="18" height="12"><rect width="18" height="12" fill="#fff"/><rect y="1.5" width="18" height="1.5" fill="#0038b8"/><rect y="9" width="18" height="1.5" fill="#0038b8"/></svg>Hebrew</span>
  </div>
  <h3>Meet The Team</h3>
  <div class="team">
    <div class="member"><div class="photo" role="img" aria-label="Portrait of John Cole"></div><h4>John Cole</h4><div class="role">Maecenas vel</div><p class="bio">Gentle care and steady guidance for every stage of life, with calm sessions built around you.</p><div class="book">MAKE AN APPOINTMENT</div></div>
    <div class="member"><div class="photo warm" role="img" aria-label="Portrait of Sophia"></div><h4>Sophia</h4><div class="role">Maecenas vel</div><p class="bio">Gentle care and steady guidance for every stage of life, with calm sessions built around you.</p><div class="book">MAKE AN APPOINTMENT</div></div>
    <div class="member"><div class="photo" role="img" aria-label="Portrait of Daniel"></div><h4>Daniel</h4><div class="role">Maecenas vel</div><p class="bio">Gentle care and steady guidance for every stage of life, with calm sessions built around you.</p><div class="book">MAKE AN APPOINTMENT</div></div>
    <div class="member"><div class="photo warm" role="img" aria-label="Portrait of Emma"></div><h4>Emma</h4><div class="role">Maecenas vel</div><p class="bio">Gentle care and steady guidance for every stage of life, with calm sessions built around you.</p><div class="book">MAKE AN APPOINTMENT</div></div>
    <div class="member"><div class="photo" role="img" aria-label="Portrait of Jayden"></div><h4>Jayden</h4><div class="role">Maecenas vel</div><p class="bio">Gentle care and steady guidance for every stage of life, with calm sessions built around you.</p><div class="book">MAKE AN APPOINTMENT</div></div>
  </div>
</section>

<section class="services">
  <h2>Services</h2>
  <ul class="svc-list">
    <li class="current"><svg width="22" height="22"><rect x="3" y="9" width="16" height="8" rx="4" fill="#8fb4ff"/></svg>Medication management</li>
    <li><svg width="22" height="22"><circle cx="11" cy="11" r="8" fill="#8fb4ff"/></svg>Psychotherapy: Individual, group, couples, and family</li>
    <li><svg width="22" height="22"><path d="M3 15c4-10 12-10 16 0z" fill="#8fb4ff"/></svg>Art Therapy</li>
    <li><svg width="22" height="22"><circle cx="11" cy="11" r="8" fill="none" stroke="#8fb4ff" stroke-width="2.5"/></svg>Treatment Approach</li>
    <li><svg width="22" height="22"><path d="M3 5h16M3 11h16M3 17h16" stroke="#8fb4ff" stroke-width="2.5"/></svg>Treatment Areas</li>
  </ul>
  <div class="svc-photo" role="img" aria-label="Doctor in a white coat with stethoscope writing beside medicine bottles"></div>
  <div class="svc-caption">
    <h3>MEDICATION MANAGEMENT</h3>
    <p>Careful review of every prescription, regular check-ins and clear answers so each treatment plan stays safe, simple and right for you over time.</p>
  </div>
</section>

<section class="reads">
  <h2>Good Reads</h2>
  <article class="post" style="top:130px">
    <div class="thumb book" role="img" aria-label="Open book with fanned pages"></div>
    <div class="body">
      <h3>Donec interdum neque pharetra eros faucibus</h3>
      <div class="author">Michael</div>
      <p>Birchline Realty Group is a full service real estate brokerage firm located in Lakewood, NY and Bay Village, FL. We specialize in multifamily sales and leasing; short-sales and 1031 Exchange property appropriation. With more than 12 years of experience we have had transactions in every one of Lakewood's zip codes...<br><span class="more">READ MORE</span></p>
    </div>
  </article>
  <article class="post" style="top:340px">
    <div class="thumb mags" role="img" aria-label="Stack of colourful magazines"></div>
    <div class="body">
      <h3>Donec interdum neque pharetra eros faucibus</h3>
      <div class="author">Madison</div>
      <p>Birchline Realty Group is a full service real estate brokerage firm located in Lakewood, NY and Bay Village, FL. We specialize in multifamily sales and leasing; short-sales and 1031 Exchange property appropriation. With more than 12 years of experience we have had transactions in every one of Lakewood's zip codes...<br><span class="more">READ MORE</span></p>
    </div>
  </article>
</section>

<section class="appointment">
  <h2>Appointment Request</h2>
  <div class="field" style="left:145px;top:135px;width:218px;height:38px">First Name</div>
  <div class="field" style="left:376px;top:135px;width:218px;height:38px">Last Name</div>
  <div class="field" style="left:606px;top:135px;width:218px;height:38px">Email</div>
  <div class="field" style="left:837px;top:135px;width:218px;height:38px">Tel</div>
  <div class="field" style="left:145px;top:185px;width:910px;height:120px">Message</div>
  <div class="submit">Submit</div>
</section>

<section class="map" role="img" aria-label="Street map around the clinic location in Solon, Ohio">
  <svg class="pin" width="22" height="30"><path d="M11 29C4 18 1 14 1 10a10 10 0 0120 0c0 4-3 8-10 19z" fill="#e53935"/><circle cx="11" cy="10" r="4" fill="#9b1b1b"/></svg>
</section>

<div class="contact-bar">
  <span><svg width="12" height="16"><path d="M6 15C2 9 1 7 1 5.5a5 5 0 0110 0C11 7 10 9 6 15z" fill="#fff"/></svg>4820 Maple Crest Road, Suite 210, Solon, OH 44139</span>
  <span><svg width="14" height="14"><path d="M3 1l3 3-2 2c1 2 2 3 4 4l2-2 3 3-2 2C6 13 1 8 1 3z" fill="#fff"/></svg>(440) 555-0172</span>
  <span><svg width="16" height="12"><rect x="1" y="1" width="14" height="10" fill="#fff"/><path d="M1 1l7 6 7-6" fill="none" stroke="#3d3f42" stroke-width="1.2"/></svg>hello@elleryharmony.com</span>
</div>

<footer class="site-footer">
  <div class="foot-mark"></div>
  <div class="foot-links"><span>Home</span><i>|</i><span>About Us</span><i>|</i><span>Services</span><i>|</i><span>Good Reads</span><i>|</i><span>Contact</span></div>
  <div class="copyright">Copyright © 2019 Dr Ellery Harmony Center. All rights reserved.</div>
  <div class="social"><span></span><span></span></div>
</footer>

</body>
</html>
```